"Pillowtide Chews" is the brand name for CBN infused Gummies for a restful sleep

Need a label for the glass jar and a round label for the lid. The gummy shapes are crescent white mons and blue stars or gummy sheep

You can use an 6 or 8 oz clear jar. Your illustration program should have this mock up.

Font styles to use
Sans Serif

```html
<!DOCTYPE html>
<html lang="en">
<head>
<meta charset="utf-8">
<title>Pillowtide Chews – Jar Labels</title>
<link rel="stylesheet" href="https://fonts.googleapis.com/css2?family=Raleway:wght@400;600;800&family=Roboto+Condensed:wght@700&display=swap">
<style>
  :root {
    --stage: #4a4a4a;
    --navy: #14234f;
    --berry: #d9000a;
    --dusk: #4a6298;
    --crimson: #cf3339;
    --amber: #fbb311;
    --ink: #0d1a3d;
    --white: #ffffff;
    --black: #111111;
    --moon: #f8b117;
    --cloud: #eef1f6;
  }
  html, body {
    margin: 0;
    width: 1200px;
    height: 751px;
    overflow: hidden;
    background: var(--stage);
  }
  .label-row {
    position: absolute;
    top: 252px;
    left: 0;
    width: 1200px;
    display: flex;
    justify-content: center;
    gap: 38px;
  }
  .jar-label {
    width: 335px;
    height: 315px;
    display: block;
  }
  .jar-label .band { fill: var(--band); }
  .jar-label .seal { fill: var(--seal); stroke: var(--white); stroke-width: 2.5; }
  .jar-label .leaf-mark { fill: var(--leaf); }
  .brand-name {
    font-family: "Raleway", sans-serif;
    font-weight: 800;
    font-size: 33px;
    fill: var(--white);
  }
  .brand-sub {
    font-family: "Raleway", sans-serif;
    font-weight: 800;
    font-size: 24px;
    fill: var(--white);
    letter-spacing: 0.5px;
  }
  .tagline {
    font-family: "Raleway", sans-serif;
    font-weight: 600;
    font-size: 15px;
    fill: var(--tag);
    letter-spacing: 0.5px;
  }
  .dose-figure {
    font-family: "Roboto Condensed", sans-serif;
    font-weight: 700;
    font-size: 22px;
    fill: var(--white);
  }
  .dose-unit { font-size: 13px; }
  .dose-caption {
    font-family: "Raleway", sans-serif;
    font-weight: 400;
    font-size: 12px;
    fill: var(--white);
  }
  .variant-berry { --band: var(--navy); --seal: var(--berry); --leaf: var(--white); --tag: var(--white); }
  .variant-dusk { --band: var(--navy); --seal: var(--dusk); --leaf: var(--black); --tag: var(--white); }
  .variant-amber { --band: var(--crimson); --seal: var(--amber); --leaf: var(--black); --tag: var(--ink); }
</style>
</head>
<body>
<main class="label-row">

  <svg class="jar-label variant-berry" viewBox="0 0 335 315" aria-label="Pillowtide Chews label, red seal">
    <defs>
      <linearGradient id="night-scene-a" x1="0" y1="0" x2="1" y2="1">
        <stop offset="0" stop-color="#eef1f6"/>
        <stop offset="0.55" stop-color="#f8b117"/>
        <stop offset="1" stop-color="#eef1f6"/>
      </linearGradient>
      <path id="tag-arc-a" d="M 82 252 Q 167 292 252 240"/>
    </defs>
    <rect class="band" width="335" height="315"/>
    <circle class="seal" cx="167.5" cy="157" r="134"/>
    <g role="img" aria-label="Leaf icon"><ellipse class="leaf-mark" cx="167.5" cy="63" rx="22" ry="21"/></g>
    <text class="brand-name" x="167.5" y="128" text-anchor="middle" textLength="228" lengthAdjust="spacingAndGlyphs">PILLOWTIDE</text>
    <text class="brand-sub" x="167.5" y="166" text-anchor="middle">CHEWS</text>
    <g role="img" aria-label="Illustration of a crescent moon with clouds and stars"><rect x="110" y="172" width="125" height="76" rx="30" fill="url(#night-scene-a)"/></g>
    <text class="tagline"><textPath href="#tag-arc-a" startOffset="50%" text-anchor="middle">RESTFUL SLEEP</textPath></text>
    <text class="dose-figure" x="20" y="276">30<tspan class="dose-unit">mg</tspan></text>
    <text class="dose-caption" x="21" y="294">CBN infused</text>
    <text class="dose-figure" x="315" y="276" text-anchor="end">280<tspan class="dose-unit">mg</tspan></text>
    <text class="dose-caption" x="315" y="294" text-anchor="end">Calories</text>
  </svg>

  <svg class="jar-label variant-dusk" viewBox="0 0 335 315" aria-label="Pillowtide Chews label, blue seal">
    <defs>
      <linearGradient id="night-scene-b" x1="0" y1="0" x2="1" y2="1">
        <stop offset="0" stop-color="#eef1f6"/>
        <stop offset="0.55" stop-color="#f8b117"/>
        <stop offset="1" stop-color="#eef1f6"/>
      </linearGradient>
      <path id="tag-arc-b" d="M 82 252 Q 167 292 252 240"/>
    </defs>
    <rect class="band" width="335" height="315"/>
    <circle class="seal" cx="167.5" cy="157" r="134"/>
    <g role="img" aria-label="Leaf icon"><ellipse class="leaf-mark" cx="167.5" cy="63" rx="22" ry="21"/></g>
    <text class="brand-name" x="167.5" y="128" text-anchor="middle" textLength="228" lengthAdjust="spacingAndGlyphs">PILLOWTIDE</text>
    <text class="brand-sub" x="167.5" y="166" text-anchor="middle">CHEWS</text>
    <g role="img" aria-label="Illustration of a crescent moon with clouds and stars"><rect x="110" y="172" width="125" height="76" rx="30" fill="url(#night-scene-b)"/></g>
    <text class="tagline"><textPath href="#tag-arc-b" startOffset="50%" text-anchor="middle">RESTFUL SLEEP</textPath></text>
    <text class="dose-figure" x="20" y="276">30<tspan class="dose-unit">mg</tspan></text>
    <text class="dose-caption" x="21" y="294">CBN infused</text>
    <text class="dose-figure" x="315" y="276" text-anchor="end">280<tspan class="dose-unit">mg</tspan></text>
    <text class="dose-caption" x="315" y="294" text-anchor="end">Calories</text>
  </svg>

  <svg class="jar-label variant-amber" viewBox="0 0 335 315" aria-label="Pillowtide Chews label, amber seal">
    <defs>
      <linearGradient id="night-scene-c" x1="0" y1="0" x2="1" y2="1">
        <stop offset="0" stop-color="#eef1f6"/>
        <stop offset="0.55" stop-color="#14234f"/>
        <stop offset="1" stop-color="#eef1f6"/>
      </linearGradient>
      <path id="tag-arc-c" d="M 82 252 Q 167 292 252 240"/>
    </defs>
    <rect class="band" width="335" height="315"/>
    <circle class="seal" cx="167.5" cy="157" r="134"/>
    <g role="img" aria-label="Leaf icon"><ellipse class="leaf-mark" cx="167.5" cy="63" rx="22" ry="21"/></g>
    <text class="brand-name" x="167.5" y="128" text-anchor="middle" textLength="228" lengthAdjust="spacingAndGlyphs">PILLOWTIDE</text>
    <text class="brand-sub" x="167.5" y="166" text-anchor="middle">CHEWS</text>
    <g role="img" aria-label="Illustration of a navy crescent moon with clouds and stars"><rect x="110" y="172" width="125" height="76" rx="30" fill="url(#night-scene-c)"/></g>
    <text class="tagline"><textPath href="#tag-arc-c" startOffset="50%" text-anchor="middle">RESTFUL SLEEP</textPath></text>
    <text class="dose-figure" x="20" y="276">30<tspan class="dose-unit">mg</tspan></text>
    <text class="dose-caption" x="21" y="294">CBN infused</text>
    <text class="dose-figure" x="315" y="276" text-anchor="end">280<tspan class="dose-unit">mg</tspan></text>
    <text class="dose-caption" x="315" y="294" text-anchor="end">Calories</text>
  </svg>

</main>
</body>
</html>
```